Brushline Cookout Product Labeling

We need a label design for a new product we are launching. We have developed a cooking bag that will cook your fish or game bird instantly. This is for the everyday fisherman and upland game hunter. This label will be printed on a thin sticker on the front of a Velnex Bag. The Velnex Bag is 9 1/2 x 12 inches. Inside the Velnex Bag is 3 cooking bags.
Target Market(s)
hunters and fishermen
Industry/Entity Type
Cooking
Font styles to use
Sans Serif
Colors
Designer to choose colors to be used in the design.
Requirements
Must have
- It must have "Brushline Cookout" logo. It should have Reed and Ridge. Reed and Ridge is the type of seasoning. It must have a small place on the label for net weight. It must also have the wording "Contains: 3 Individual Cooking Bags Inside.
Nice to have
- I really like a topographical map in the background. I have attached several images with products like that. It could also be cool having the background of the bag with a tiger trout's scales. I attached some images of that too. Some other ideas I thought i have is having a picture of the bird and fish on the bag. There is an GIF attached that has a cool looking fish that did that. There is also an image of a Brovik product that did the same thing.

```html
<!DOCTYPE html>
<html lang="en">
<head>
<meta charset="utf-8">
<title>Brushline Cookout – Reed and Ridge Label</title>
<link rel="stylesheet" href="https://fonts.googleapis.com/css2?family=Oswald:wght@600&family=Cabin+Condensed:wght@500;600&display=swap">
<style>
  :root {
    --page: #ffffff;
    --label-orange: #f15a22;
    --label-dark: #1e1e1e;
    --label-dark-soft: #2a2a2a;
    --grid-line: rgba(241, 90, 34, 0.3);
    --text-light: #ffffff;
    --art-tone: #e4582a;
    --art-deep: #a8401d;
  }
  * { margin: 0; padding: 0; box-sizing: border-box; }
  html, body {
    width: 1200px; height: 675px; overflow: hidden;
    background: var(--page);
  }
  .canvas { position: relative; width: 1200px; height: 675px; }

  .label {
    position: absolute; left: 400px; top: 90px;
    width: 386px; height: 486px;
  }
  .label-shape { display: block; width: 386px; height: 486px; }
  .label-frame { fill: var(--label-orange); }
  .label-base { fill: var(--label-dark); }
  .label-grid { fill: url(#grid-cells); }
  .label-tone { fill: url(#panel-tone); }
  .grid-rule { stroke: var(--grid-line); stroke-width: 1; fill: none; }

  .brand-name {
    position: absolute; left: 400px; width: 386px; top: 243px;
    text-align: center;
    font-family: "Oswald", sans-serif; font-weight: 600;
    font-size: 37px; letter-spacing: -0.6px; line-height: 1.2;
    color: var(--text-light); text-transform: uppercase;
  }
  .seasoning-name {
    position: absolute; left: 400px; width: 386px; top: 342px;
    text-align: center;
    font-family: "Cabin Condensed", sans-serif; font-weight: 600;
    font-size: 42px; line-height: 1;
    color: var(--text-light); text-transform: uppercase;
  }
  .seasoning-name .joiner { font-size: 29px; }

  .art { position: absolute; border-radius: 6px; }
  .art-fish {
    left: 518px; top: 398px; width: 66px; height: 80px;
    background: radial-gradient(ellipse at 50% 50%, var(--art-tone) 0%, var(--art-deep) 55%, rgba(30,30,30,0) 78%);
  }
  .art-bird {
    left: 606px; top: 394px; width: 116px; height: 82px;
    background: radial-gradient(ellipse at 45% 55%, var(--art-tone) 0%, var(--art-deep) 55%, rgba(30,30,30,0) 78%);
  }

  .contents {
    position: absolute; left: 400px; width: 386px; top: 489px;
    text-align: center;
    font-family: "Cabin Condensed", sans-serif; font-weight: 500;
    font-size: 16.5px; letter-spacing: -0.2px;
    color: var(--label-orange); text-transform: uppercase;
  }
  .contents .lead { font-size: 11px; }
  .net-weight {
    position: absolute; left: 400px; width: 386px; top: 519px;
    text-align: center;
    font-family: "Cabin Condensed", sans-serif; font-weight: 600;
    font-size: 29px; line-height: 1.1; color: var(--label-orange);
  }
  .net-weight .unit { font-size: 16px; }
</style>
</head>
<body>
<main class="canvas">
  <section class="label">
    <svg class="label-shape" viewBox="0 0 386 486" aria-hidden="true">
      <defs>
        <clipPath id="panel-edge">
          <path d="M12,14 L40,11 L70,13 L95,10 L130,12 L160,9 L200,12 L235,10 L270,13 L300,10 L335,12 L360,9 L372,11 L378,16 L376,50 L379,90 L375,140 L378,190 L376,240 L379,290 L375,340 L378,390 L376,440 L378,470 L372,478 L340,476 L300,479 L260,476 L220,480 L180,477 L140,479 L100,476 L60,479 L25,477 L12,478 L9,460 L12,420 L8,380 L11,330 L9,280 L12,230 L8,180 L11,130 L9,80 L12,40 Z"/>
        </clipPath>
        <pattern id="grid-cells" x="22" y="8" width="50" height="46" patternUnits="userSpaceOnUse">
          <path class="grid-rule" d="M0,0.5 H50 M0.5,0 V46"/>
        </pattern>
        <radialGradient id="panel-tone" cx="50%" cy="45%" r="70%">
          <stop offset="0%" stop-color="#2c2c2c" stop-opacity="0.9"/>
          <stop offset="60%" stop-color="#222222" stop-opacity="0.5"/>
          <stop offset="100%" stop-color="#151515" stop-opacity="0.9"/>
        </radialGradient>
      </defs>
      <rect class="label-frame" x="0" y="0" width="386" height="486" rx="14"/>
      <g clip-path="url(#panel-edge)" role="img" aria-label="Topographic map texture background">
        <rect class="label-base" x="0" y="0" width="386" height="486"/>
        <rect class="label-tone" x="0" y="0" width="386" height="486"/>
        <rect class="label-grid" x="0" y="0" width="386" height="486"/>
      </g>
    </svg>
  </section>

  <h1 class="brand-name">Brushline Cookout</h1>
  <h2 class="seasoning-name">Reed <span class="joiner">and</span> Ridge</h2>

  <div class="art art-fish" role="img" aria-label="Orange engraved illustration of a leaping trout"></div>
  <div class="art art-bird" role="img" aria-label="Orange engraved illustration of a pheasant"></div>

  <p class="contents"><span class="lead">Contains:</span> 3 Individual Cooking Bags Inside</p>
  <p class="net-weight">100 <span class="unit">G</span></p>
</main>
</body>
</html>
```